ALL TEXT GRAPHICS RK May 2025 for Instagram

We are looking for a series of social media graphics for Instagram (new size: 4:5 (1080 x 1350 pixels) ratio that are ALL TEXT. We want the following quotes below on each graphic; one quote per graphic. AND, In very small letters at the bottom of each graphic, add @RKBexleyOnline
The look and feel of these graphics should be complimentary to the color palette attached below; but keep them simple. But the design is up to you; at the end of this document, I provided various samples of all text graphics that I like as examples.
women looking to lose weight

```html
<!DOCTYPE html>
<html lang="en">
<head>
<meta charset="utf-8">
<title>RK Instagram Text Graphics</title>
<link rel="stylesheet" href="https://fonts.googleapis.com/css2?family=League+Gothic&family=Outfit:wght@400;500;600&display=swap">
<style>
  :root {
    --board: #c8c8c8;
    --card-light: #fdf1f6;
    --card-mid: #fbe2ed;
    --card-deep: #f8d3e3;
    --magenta: #d0106c;
    --frame: #e2347f;
    --ink: #1b1b1b;
    --shadow: rgba(90, 0, 35, 0.35);
  }
  * { box-sizing: border-box; margin: 0; padding: 0; }
  html, body { width: 1200px; height: 3352px; overflow: hidden; }
  body { background: var(--board); position: relative; }

  .sheet {
    position: absolute;
    left: 99px; top: 101px;
    display: grid;
    grid-template-columns: 495px 495px;
    grid-auto-rows: 618px;
    column-gap: 12px;
    row-gap: 14px;
  }

  .post {
    position: relative;
    overflow: hidden;
    background:
      radial-gradient(ellipse 60% 40% at 20% 15%, var(--card-deep) 0%, transparent 70%),
      radial-gradient(ellipse 55% 45% at 85% 70%, var(--card-mid) 0%, transparent 70%),
      radial-gradient(ellipse 50% 35% at 30% 90%, var(--card-mid) 0%, transparent 70%),
      var(--card-light);
  }

  .post__frame {
    position: absolute;
    left: 36px; top: 32px; right: 35px; bottom: 30px;
    border: 2px solid var(--frame);
  }

  .post__handle {
    position: absolute;
    left: 0; right: 0; bottom: 22px;
    text-align: center;
    font: 600 16px/16px "Outfit", sans-serif;
    color: var(--ink);
  }
  .post__handle span {
    background: #fcebf2;
    padding: 0 10px;
  }

  .post__copy {
    position: absolute;
    left: 52px; right: 40px;
  }

  .headline {
    font-family: "League Gothic", "Oswald", sans-serif;
    color: var(--magenta);
    text-transform: uppercase;
    line-height: 0.98;
    text-shadow: 2px 2px 0 var(--shadow);
    white-space: nowrap;
  }

  .body-copy {
    font-family: "Outfit", sans-serif;
    font-weight: 400;
    color: var(--ink);
    line-height: 1.22;
    margin-top: 18px;
  }
  .keyword { color: var(--magenta); font-weight: 600; }
</style>
</head>
<body>
<main class="sheet">

  <article class="post">
    <div class="post__frame"></div>
    <div class="post__copy" style="top:150px">
      <h2 class="headline" style="font-size:79px">Tired. Moody.</h2>
      <p class="headline" style="font-size:63px">Stubborn Belly Fat.</p>
      <p class="body-copy" style="font-size:38px">Your Hormones Are<br>Screaming For Help!<br>Let’s Fix That.</p>
    </div>
    <p class="post__handle"><span>@RKBexleyOnline</span></p>
  </article>

  <article class="post">
    <div class="post__frame"></div>
    <div class="post__copy" style="top:106px;left:60px">
      <h2 class="headline" style="font-size:78px">That Stubborn<br>Weight?</h2>
      <p class="headline" style="font-size:64px;margin-top:8px">It’s Not Your Fault.</p>
      <p class="body-copy" style="font-size:38px;line-height:1.15">Your Hormones Are<br>To Blame And<br>You’re Not Alone;<br>But There Is A Fix.</p>
    </div>
    <p class="post__handle"><span>@RKBexleyOnline</span></p>
  </article>

  <article class="post">
    <div class="post__frame"></div>
    <div class="post__copy" style="top:112px">
      <h2 class="headline" style="font-size:57px">Your Belly Isn’t Fat...</h2>
      <p class="headline" style="font-size:82px">It’s Hormonal.<br>And Here’s<br>How To Fix It.</p>
      <p class="body-copy" style="font-size:33px">Comment <span class="keyword">HORMONES</span><br>If Nothing Is Working.</p>
    </div>
    <p class="post__handle"><span>@RKBexleyOnline</span></p>
  </article>

  <article class="post">
    <div class="post__frame"></div>
    <div class="post__copy" style="top:100px;left:60px">
      <h2 class="headline" style="font-size:80px">The Stubborn</h2>
      <p class="headline" style="font-size:112px;line-height:0.9">Belly Fat<br>After 40?</p>
      <p class="body-copy" style="font-size:34px;line-height:1.15">It’s Not About<br>Calories; It’s About<br>Your Hormones.?<br>Here is the fix!</p>
    </div>
    <p class="post__handle"><span>@RKBexleyOnline</span></p>
  </article>

  <article class="post">
    <div class="post__frame"></div>
    <div class="post__copy" style="top:110px;left:64px">
      <h2 class="headline" style="font-size:78px">Flat Tummy In<br>Your 40s?</h2>
      <p class="headline" style="font-size:64px;margin-top:8px">It’s Still Possible!</p>
      <p class="body-copy" style="font-size:33px">Comment <span class="keyword">BYE BELLY</span><br>To Get The 10 Secrets<br>To A Flatter Tummy</p>
    </div>
    <p class="post__handle"><span>@RKBexleyOnline</span></p>
  </article>

  <article class="post">
    <div class="post__frame"></div>
    <div class="post__copy" style="top:110px;left:56px">
      <h2 class="headline" style="font-size:82px">Bloating.<br>Muffin Top.</h2>
      <p class="headline" style="font-size:68px;margin-top:8px">Puffy Waistline.</p>
      <p class="body-copy" style="font-size:31px">Your Body’s Screaming For<br>A Different Kind Of Fix.<br>Here It Is</p>
    </div>
    <p class="post__handle"><span>@RKBexleyOnline</span></p>
  </article>

  <article class="post">
    <div class="post__frame"></div>
    <div class="post__copy" style="top:130px">
      <h2 class="headline" style="font-size:68px">You’re Doing All<br>The “Right” Things,<br>But Your Belly<br>Won’t Go Down?</h2>
      <p class="body-copy" style="font-size:36px">Here’s What You<br>Haven’t Tried.</p>
    </div>
    <p class="post__handle"><span>@RKBexleyOnline</span></p>
  </article>

  <article class="post">
    <div class="post__frame"></div>
    <div class="post__copy" style="top:88px;left:60px">
      <h2 class="headline" style="font-size:77px">This 90-Day<br>Plan Helped<br>Women Over 40<br>Slim Down,</h2>
      <p class="body-copy" style="font-size:35px">Get A Tiny Waist And<br>Feel Sexy Again.<br>You’re Next.</p>
    </div>
    <p class="post__handle"><span>@RKBexleyOnline</span></p>
  </article>

  <article class="post">
    <div class="post__frame"></div>
    <div class="post__copy" style="top:92px;left:60px">
      <h2 class="headline" style="font-size:65px">This Is The Secret<br>Women Over 40<br>Are Using To<br>Get Snatched;<br>Without Starving.</h2>
      <p class="body-copy" style="font-size:35px">Comment <span class="keyword">SKINNY</span> To<br>Get The Exact Plan.</p>
    </div>
    <p class="post__handle"><span>@RKBexleyOnline</span></p>
  </article>

  <article class="post">
    <div class="post__frame"></div>
    <div class="post__copy" style="top:138px;left:68px">
      <h2 class="headline" style="font-size:64px">What Worked<br>In Your 30s<br>Won’t Work Now.</h2>
      <p class="body-copy" style="font-size:32px;margin-top:30px">Here’s what actually<br>does. Drop 30 Pounds<br>in 3 Months.</p>
    </div>
    <p class="post__handle"><span>@RKBexleyOnline</span></p>
  </article>

</main>
</body>
</html>
```